Auto Mechanic business card

Need a general business card for Kestrelworks.
Name on card should be 'Tidewell Garage'
Tel # (869) 555 0142
Address is - Palm Lane, Basseterre, St. Kitts
Whatsapp and facebook symbols should be added
On back of card should include services offered
General Repairs
Brakes
Tune Ups
Suspensions
Oil Leaks
Dent repairs
Suspensions
Car Sales
Tyre Repairs
General service
Check Engine Light
Minor Electricals

Target Market(s)

General Population, University students

Industry/Entity Type

Auto Mechanic

Contact Information for Business Card

Tidewell Garage

Requirements
Must have
• 2 Sides

```html
<!DOCTYPE html>
<html lang="en">
<head>
<meta charset="utf-8">
<title>Tidewell Garage – Business Card</title>
<link rel="stylesheet" href="https://fonts.googleapis.com/css2?family=Chakra+Petch:wght@500;600;700&display=swap">
<style>
  :root {
    --backdrop: #e21e26;
    --plate: #d9dadc;
    --plate-light: #e6e7e9;
    --ink: #0d0d0d;
    --accent: #e21e26;
    --band-dark: #0a0a0a;
  }
  * { box-sizing: border-box; margin: 0; padding: 0; }
  html, body {
    width: 1200px; height: 900px; overflow: hidden;
    background: var(--backdrop);
    font-family: "Chakra Petch", sans-serif;
    color: var(--ink);
  }
  .card {
    position: absolute; left: 284px; width: 632px; height: 361px;
    border-radius: 22px; overflow: hidden;
  }
  .card--back { top: 80px; }
  .card--front { top: 459px; }
  .card__plate {
    position: absolute; inset: 0;
    background: linear-gradient(160deg, var(--plate-light), var(--plate) 60%);
  }
  .card__band {
    position: absolute; left: 0; right: 0; bottom: 0; height: 11px;
    display: flex;
  }
  .card__band-red { background: var(--accent); }
  .card__band-dark { background: var(--band-dark); flex: 1; clip-path: polygon(3px 0, 100% 0, 100% 100%, 0 100%); margin-left: -3px; }
  .card--back .card__band-red { width: 404px; }
  .card--front .card__band-red { width: 222px; }

  .services { position: absolute; top: 78px; }
  .services--repairs { left: 71px; }
  .services--general { left: 357px; }
  .services__title { font-size: 18px; font-weight: 700; letter-spacing: .4px; line-height: 1; margin-bottom: 14px; }
  .services__list { list-style: none; }
  .services__item { font-size: 17.5px; font-weight: 500; letter-spacing: .9px; line-height: 22.6px; }
  .services__item::before { content: "»"; display: inline-block; width: 20px; }

  .brand-name { position: absolute; font-weight: 700; color: var(--ink); white-space: nowrap; line-height: 1; }
  .brand-name--small { right: 71px; top: 276px; font-size: 24px; letter-spacing: .5px; }
  .brand-name--large { left: 71px; top: 64px; font-size: 50px; letter-spacing: 1px; }

  .contact { position: absolute; left: 71px; }
  .contact__phone { top: 140px; font-size: 27px; font-weight: 500; letter-spacing: 1px; }
  .contact__address { top: 180px; font-size: 17.5px; font-weight: 500; letter-spacing: 1px; line-height: 21px; }
  .social { position: absolute; left: 71px; top: 245px; display: flex; gap: 4px; }
  .social__dot { width: 28px; height: 28px; border-radius: 50%; background: var(--accent); }
</style>
</head>
<body>
  <section class="card card--back" aria-label="Card back: services">
    <div class="card__plate" role="img" aria-label="Brushed diamond-plate metal texture"></div>
    <div class="services services--repairs">
      <h2 class="services__title">GENERAL REPAIRS</h2>
      <ul class="services__list">
        <li class="services__item">BRAKES TUNE UPS</li>
        <li class="services__item">SUSPENSIONS</li>
        <li class="services__item">OIL LEAKS</li>
        <li class="services__item">DENT REPAIRS</li>
        <li class="services__item">SUSPENSIONS</li>
        <li class="services__item">CAR SALES</li>
        <li class="services__item">TYRE REPAIRS</li>
      </ul>
    </div>
    <div class="services services--general">
      <h2 class="services__title">GENERAL SERVICE</h2>
      <ul class="services__list">
        <li class="services__item">CHECK ENGINE LIGHT</li>
        <li class="services__item">MINOR ELECTRICALS</li>
      </ul>
    </div>
    <p class="brand-name brand-name--small">TIDEWELL GARAGE</p>
    <div class="card__band"><div class="card__band-red"></div><div class="card__band-dark"></div></div>
  </section>

  <section class="card card--front" aria-label="Card front: contact">
    <div class="card__plate" role="img" aria-label="Brushed diamond-plate metal texture"></div>
    <h1 class="brand-name brand-name--large">TIDEWELL GARAGE</h1>
    <p class="contact contact__phone">(869) 555 0142</p>
    <p class="contact contact__address">PALM LANE, BASSETERRE,<br>ST. KITTS</p>
    <div class="social" aria-label="Messaging and social profiles">
      <span class="social__dot"></span>
      <span class="social__dot"></span>
    </div>
    <div class="card__band"><div class="card__band-red"></div><div class="card__band-dark"></div></div>
  </section>
</body>
</html>
```